BHSC Business cards

We are an established dental practice that is looking for new business cards to match our new logo. We are looking for something unique and sophisticated.
BRIEF: Colours are black, silver and white. Include the company name, logo (including “Pelwick Heath Dental Care”) and phone number “03 9415 2876”.
Front - Include the company name, logo (including “Pelwick Heath Dental Care”) and phone number “03 9415 2876”.
Back - Include the company name,  “Pelwick Heath Dental Care”, phone number “03 9415 2876”. address "64A Tindle Street, Pelwick Heath, Vic 3187", "Email reception@pelwickheathdentalcare.com.au", the Dentist Name " Dr ................................"  Your next appointment "Day, date and time(am/pm)".  3 lines for 3 appointments please, and at the bottom "IF UNABLE TO KEEP THIS APPOINTMENT 48 HOURS NOTICE IS REQUIRED."
Try and be creative and different with the design, i've added an image for inspiration

Target Market(s)
ALL in need of dental
Industry/Entity Type
Dental Clinic
Look and feel
Each slider illustrates characteristics of the customer's brand and the style your logo design should communicate.

```html
<!DOCTYPE html>
<html lang="en">
<head>
<meta charset="UTF-8">
<title>Pelwick Heath Dental Care – Business Card</title>
<link rel="stylesheet" href="https://fonts.googleapis.com/css2?family=Cinzel:wght@700&family=Open+Sans:wght@400;700&display=swap">
<style>
  :root {
    --ink: #231f20;
    --paper: #ffffff;
    --backdrop: #e6e8eb;
    --rule: #b9bbbe;
    --text: #2b2b2b;
  }
  * { margin: 0; padding: 0; box-sizing: border-box; }
  html, body {
    width: 1200px;
    height: 900px;
    overflow: hidden;
    background: var(--backdrop);
  }
  .canvas {
    position: relative;
    width: 1200px;
    height: 900px;
  }
  .card {
    position: absolute;
    left: 70px;
    top: 148px;
    width: 1060px;
    height: 604px;
    background: var(--paper);
    box-shadow: 0 6px 24px rgba(0,0,0,0.12);
    font-family: "Open Sans", sans-serif;
    color: var(--text);
  }
  .brand {
    position: absolute;
    left: 98px;
    top: 106px;
    display: flex;
    align-items: center;
    gap: 14px;
  }
  .brand-mark {
    width: 62px;
    height: 62px;
    border-radius: 50%;
    background: var(--ink);
    flex: none;
  }
  .brand-text {
    display: flex;
    flex-direction: column;
    color: var(--ink);
    font-weight: 700;
    line-height: 1;
  }
  .brand-name {
    font-size: 31px;
    letter-spacing: 1px;
  }
  .brand-sub {
    margin-top: 7px;
    font-size: 13.5px;
    letter-spacing: 3.2px;
    display: flex;
    align-items: center;
    gap: 6px;
  }
  .brand-phone { letter-spacing: 1.5px; }
  .person {
    position: absolute;
    right: 71px;
    top: 108px;
    text-align: center;
  }
  .person-name {
    font-family: "Cinzel", serif;
    font-weight: 700;
    font-size: 33px;
    color: var(--ink);
    line-height: 1;
    letter-spacing: 0.5px;
  }
  .person-title {
    margin-top: 4px;
    font-size: 16.5px;
    color: var(--text);
  }
  .band {
    position: absolute;
    left: 74px;
    top: 386px;
    width: 916px;
    height: 42px;
  }
  .contacts {
    position: absolute;
    left: 70px;
    top: 433px;
    list-style: none;
  }
  .contact {
    display: flex;
    align-items: center;
    gap: 9px;
    height: 31px;
    font-size: 15px;
    color: var(--text);
  }
  .contact svg { width: 26px; height: 26px; flex: none; }
  .socials {
    position: absolute;
    right: 78px;
    top: 528px;
    display: flex;
    gap: 16px;
  }
  .social {
    width: 45px;
    height: 45px;
    border: 3px solid var(--ink);
    border-radius: 2px;
  }
</style>
</head>
<body>
<main class="canvas">
  <section class="card" aria-label="Business card front">
    <div class="brand">
      <div class="brand-mark" aria-hidden="true"></div>
      <div class="brand-text">
        <span class="brand-name">PELWICK HEATH</span>
        <span class="brand-sub">DENTAL CARE <span class="brand-phone">— 03 9415 2876</span></span>
      </div>
    </div>

    <div class="person">
      <p class="person-name">MARCUS HALE</p>
      <p class="person-title">CEO/Managing Director</p>
    </div>

    <svg class="band" viewBox="0 0 916 42" aria-hidden="true">
      <line x1="0" y1="41" x2="196" y2="40" stroke="var(--rule)" stroke-width="1.2"/>
      <polygon points="237,0 916,0 916,40 194,40" fill="var(--ink)"/>
    </svg>

    <ul class="contacts">
      <li class="contact">
        <svg viewBox="0 0 26 26" aria-hidden="true">
          <circle cx="13" cy="13" r="11.5" fill="none" stroke="var(--ink)" stroke-width="1.4"/>
          <rect x="9" y="6" width="8" height="14" rx="1.5" fill="none" stroke="var(--ink)" stroke-width="1.4"/>
          <line x1="11.5" y1="17.5" x2="14.5" y2="17.5" stroke="var(--ink)" stroke-width="1.2"/>
        </svg>
        <span>214-555-0173</span>
      </li>
      <li class="contact">
        <svg viewBox="0 0 26 26" aria-hidden="true">
          <circle cx="13" cy="13" r="11.5" fill="none" stroke="var(--ink)" stroke-width="1.4"/>
          <polygon points="13,6.5 19.5,12.5 17.5,12.5 17.5,19 8.5,19 8.5,12.5 6.5,12.5" fill="var(--ink)"/>
          <rect x="11.5" y="14.5" width="3" height="4.5" fill="var(--paper)"/>
        </svg>
        <span>214-555-0173</span>
      </li>
      <li class="contact">
        <svg viewBox="0 0 26 26" aria-hidden="true">
          <circle cx="13" cy="13" r="11.5" fill="none" stroke="var(--ink)" stroke-width="1.4"/>
          <rect x="7.5" y="9" width="11" height="8" fill="var(--ink)"/>
          <polyline points="7.5,9 13,13.5 18.5,9" fill="none" stroke="var(--paper)" stroke-width="1"/>
        </svg>
        <span>marcushale@mailbox.com</span>
      </li>
    </ul>

    <div class="socials" aria-hidden="true">
      <span class="social"></span>
      <span class="social"></span>
      <span class="social"></span>
    </div>
  </section>
</main>
</body>
</html>
```